Printer Cartridges Supplier Namecard

Attached is my company logo and the design of my current namecard. I would like to have a more special look for it. Can have a little cuteness too rather than those normal standard feel. I'm a supplier mainly dealing with original and compatible printer toner cartridges, some other products like paper supplies as well.

Target Market(s)

Companies, businesses, corporates

Industry/Entity Type

It Company

Contact Information for Business Card

Logo, name, contact, address, supplies and maybe a slogan

Colors
85cae6
33a6d7
3176b5
0255a3
0792cd
85abd2

Requirements
Must have
• Logo, name, contact and address basic details.
• Must include some pictures, not just rearrange what I'm currently having.
Nice to have
• Be creative and bold, a diiferent traditional feel.

```html
<!DOCTYPE html>
<html lang="en">
<head>
<meta charset="utf-8">
<title>dotpress.sg – Business Card</title>
<link rel="stylesheet" href="https://fonts.googleapis.com/css2?family=Lato:wght@400;700&family=Quicksand:wght@500;700&display=swap">
<style>
  :root {
    --backdrop: #e9eaec;
    --card-grey: #55575a;
    --card-white: #ffffff;
    --brand-blue: #5fb3e4;
    --text-dark: #2b2b2d;
    --text-light: #ffffff;
    --icon-blue: #5fb3e4;
  }
  * { box-sizing: border-box; margin: 0; padding: 0; }
  html, body { width: 1200px; height: 900px; overflow: hidden; }
  body {
    background: var(--backdrop);
    font-family: "Lato", Arial, sans-serif;
    position: relative;
  }
  .card {
    position: absolute;
    width: 620px;
    height: 354px;
    border-radius: 4px;
    overflow: hidden;
    box-shadow: 0 10px 26px rgba(0,0,0,0.18);
  }

  /* Front side */
  .card-front { left: 110px; top: 70px; background: var(--card-grey); }
  .front-brand {
    position: absolute; left: 0; right: 0; top: 62px;
    display: flex; flex-direction: column; align-items: center;
    color: var(--text-light);
  }
  .brand-row { display: flex; align-items: center; gap: 16px; }
  .brand-mark { width: 54px; height: 54px; background: var(--brand-blue); border-radius: 8px; }
  .front-brand .brand-name { font-size: 62px; font-weight: 400; line-height: 1; color: var(--text-light); }
  .tagline { font-size: 11px; font-weight: 700; margin-top: 6px; margin-left: 70px; letter-spacing: 0.2px; }
  .service-band {
    position: absolute; left: 0; right: 0; top: 178px; height: 96px;
    background: var(--brand-blue);
    display: grid; grid-template-columns: 1fr 1fr;
    padding: 18px 40px 0 40px;
    column-gap: 20px;
  }
  .service-list { list-style: none; color: var(--text-light); font-size: 17px; line-height: 1.35; }
  .service-list li::before { content: "●"; font-size: 11px; margin-right: 8px; vertical-align: 2px; }

  /* Back side */
  .card-back { left: 470px; top: 476px; background: var(--card-white); }
  .person { position: absolute; left: 48px; top: 62px; }
  .person-name {
    font-family: "Quicksand", "Lato", sans-serif;
    font-weight: 700; font-size: 31px; color: var(--brand-blue); line-height: 1.05;
  }
  .person-role { font-size: 16px; color: var(--text-dark); margin-top: 2px; }
  .back-brand { position: absolute; right: 42px; top: 64px; display: flex; align-items: center; gap: 12px; }
  .back-brand .brand-mark { width: 48px; height: 48px; }
  .back-brand .brand-name { font-size: 50px; font-weight: 400; color: var(--card-grey); line-height: 1; }
  .contact-list { position: absolute; left: 48px; top: 168px; list-style: none; font-size: 17px; color: var(--text-dark); }
  .contact-list li { display: flex; align-items: center; gap: 8px; line-height: 1.3; }
  .contact-icon { width: 13px; height: 13px; flex: none; }
  .address { position: absolute; left: 48px; top: 246px; font-size: 18px; line-height: 1.3; color: var(--text-dark); }
  .wave { position: absolute; left: 0; bottom: 0; width: 620px; height: 354px; }
  .wave-grey { fill: var(--card-grey); }
  .wave-blue { fill: var(--brand-blue); }
</style>
</head>
<body>

  <section class="card card-front">
    <div class="front-brand">
      <div class="brand-row">
        <span class="brand-mark"></span>
        <span class="brand-name">dotpress.sg</span>
      </div>
      <p class="tagline">Compatible printer ink and toner solutions</p>
    </div>
    <div class="service-band">
      <ul class="service-list">
        <li>Printer Ink &amp; Toner Cartridges</li>
        <li>Original Printer Cartridges</li>
      </ul>
      <ul class="service-list">
        <li>Paper Products</li>
        <li>Printer Maintainence &amp; Repair</li>
      </ul>
    </div>
  </section>

  <section class="card card-back">
    <svg class="wave" viewBox="0 0 620 354" aria-hidden="true">
      <path class="wave-blue" d="M0,284 C170,334 330,300 478,210 C345,318 170,348 0,310 Z"/>
      <path class="wave-grey" d="M0,354 L0,320 C170,356 350,322 484,232 C540,194 580,182 620,178 L620,354 Z"/>
    </svg>

    <div class="person">
      <h1 class="person-name">Clara Tan</h1>
      <p class="person-role">Sales Executive</p>
    </div>

    <div class="back-brand">
      <span class="brand-mark"></span>
      <span class="brand-name">dotpress.sg</span>
    </div>

    <ul class="contact-list">
      <li>
        <svg class="contact-icon" viewBox="0 0 12 12" aria-hidden="true"><rect x="2.5" y="0.5" width="7" height="11" rx="1.5" fill="none" stroke="#5fb3e4" stroke-width="1.4"/><circle cx="6" cy="9.3" r="0.8" fill="#5fb3e4"/></svg>
        9100 4477
      </li>
      <li>
        <svg class="contact-icon" viewBox="0 0 12 12" aria-hidden="true"><rect x="0.5" y="2" width="11" height="8" fill="#5fb3e4"/><path d="M0.8,2.4 L6,6.6 L11.2,2.4" fill="none" stroke="#fff" stroke-width="1"/></svg>
        clara@dotpress.sg
      </li>
      <li>
        <svg class="contact-icon" viewBox="0 0 12 12" aria-hidden="true"><circle cx="6" cy="6" r="5.5" fill="#5fb3e4"/><path d="M0.8,6 H11.2 M6,0.6 C3,3.5 3,8.5 6,11.4 M6,0.6 C9,3.5 9,8.5 6,11.4" fill="none" stroke="#fff" stroke-width="0.8"/></svg>
        www.dotpress.sg
      </li>
    </ul>

    <p class="address">17 Harbour Row<br>#04-112, Singapore 500017</p>
  </section>

</body>
</html>
```